Bao Lotus Menu Design Project

This project is pretty straight forward. You will be given 3 files which include the following:
1. Our proposed menu
2. Our Company logo
3. A sample menu on what we are looking for design wise

Your job is to create a visually pleasing menu that is simple, clean and fresh. Please refer to our home website for additional information. (www.baolotus-example.com) Must be in eps or equivalent format.

Target Market(s)

20s to 40s

Industry/Entity Type

It Company

Requirements
Must have
• Company log
Must be in EPS format

```html
<!DOCTYPE html>
<html lang="en">
<head>
<meta charset="utf-8">
<title>Bao Lotus Menu</title>
<link href="https://fonts.googleapis.com/css2?family=Open+Sans:ital,wght@0,400;0,700;0,800;1,400&display=swap" rel="stylesheet">
<style>
:root{
  --ink:#111111;
  --mint:#2fe2a6;
  --mint-light:#5cebbb;
  --paper:#ffffff;
  --red:#e8141c;
  --black:#050505;
}
*{margin:0;padding:0;box-sizing:border-box}
html,body{width:927px;height:1200px;overflow:hidden;background:var(--paper)}
.menu{position:relative;width:900px;height:1165px;transform:scale(1.03);transform-origin:0 0;font-family:"Open Sans",Arial,sans-serif;color:var(--ink)}
.section{position:absolute}
.col-left{left:32px;width:397px}
.col-right{left:467px;width:396px}
.band{position:absolute;height:36px;display:flex;align-items:center;padding-left:6px}
.band-fill{position:absolute;inset:0;background:linear-gradient(90deg,var(--mint),var(--mint-light) 50%,var(--mint))}
.band h2{position:relative;color:var(--paper);font-size:20px;font-weight:800;letter-spacing:.2px;text-shadow:1px 1px 0 rgba(0,0,0,.35)}
.item{margin-bottom:14px}
.item-head{display:flex;justify-content:space-between;font-size:13.5px;font-weight:700;line-height:17px}
.item-head .price{font-weight:400;font-size:13px}
.item p{font-size:12px;font-style:italic;line-height:17px;padding-right:8px}
.placeholder{margin-bottom:16px}
.placeholder p{white-space:nowrap;overflow:hidden;padding-right:0;font-size:11.5px}
.teas .item p{padding-right:55px}
.sizes{display:flex;justify-content:space-between;font-size:12px;line-height:17px}
.size-grid{display:grid;grid-template-columns:28px 28px;gap:4px;text-align:right;font-size:12.5px;font-weight:400;line-height:17px}
.footer-left{position:absolute;left:0;top:1097px;width:393px;height:30px;background:var(--black)}
.footer-right{position:absolute;left:475px;top:1097px;width:425px;height:30px;background:var(--red)}
.brand{position:absolute;left:392px;top:1066px;width:84px;height:94px;border:2px solid var(--black);background:var(--paper);display:flex;align-items:center;justify-content:center;text-align:center;font-size:16px;font-weight:800;line-height:18px;color:var(--red)}
</style>
</head>
<body>
<main class="menu">

  <section class="section col-left" style="top:30px">
    <div class="item"><div class="item-head"><span>Bok Choy With Black Mushrooms</span><span class="price">6.95</span></div><p>Baby bokchoy and black mushrooms sautéed in a brown sauce.</p></div>
    <div class="item"><div class="item-head"><span>Spicy Garlic Eggplant</span><span class="price">8.95</span></div><p>Sautéed chinese eggplant, red onions, and scallions in a spicy garlic sauce.</p></div>
    <div class="item"><div class="item-head"><span>Salt And Pepper Tofu</span><span class="price">7.95</span></div><p>Lightly battered soft tofu cubes with a pepper spice with bell peppers and white crunchies.</p></div>
    <div class="item"><div class="item-head"><span>Spinach With Garlic</span><span class="price">6.95</span></div><p>Sautéed spinach with garlic.</p></div>
  </section>

  <div class="band" style="left:25px;top:265px;width:416px"><span class="band-fill" role="img" aria-label="Mint geometric pattern band"></span><h2>*GLUTEN FREE</h2></div>

  <section class="section col-left" style="top:309px">
    <div class="item placeholder"><div class="item-head"><span>XXXXXXXX</span><span class="price">zzzz</span></div><p>yyyyyyyyyyyyyyyyyyyyyyyyyyyyyyyyyyyyyyyyyyyyyyyyyyyyyyyyyyyyyyyyyyy</p></div>
    <div class="item placeholder"><div class="item-head"><span>XXXXXXXX</span><span class="price">zzzz</span></div><p>yyyyyyyyyyyyyyyyyyyyyyyyyyyyyyyyyyyyyyyyyyyyyyyyyyyyyyyyyyyyyyyyyyy</p></div>
    <div class="item placeholder"><div class="item-head"><span>XXXXXXXX</span><span class="price">zzzz</span></div><p>yyyyyyyyyyyyyyyyyyyyyyyyyyyyyyyyyyyyyyyyyyyyyyyyyyyyyyyyyyyyyyyyyyy</p></div>
    <div class="item placeholder"><div class="item-head"><span>XXXXXXXX</span><span class="price">zzzz</span></div><p>yyyyyyyyyyyyyyyyyyyyyyyyyyyyyyyyyyyyyyyyyyyyyyyyyyyyyyyyyyyyyyyyyyy</p></div>
    <div class="item placeholder"><div class="item-head"><span>XXXXXXXX</span><span class="price">zzzz</span></div><p>yyyyyyyyyyyyyyyyyyyyyyyyyyyyyyyyyyyyyyyyyyyyyyyyyyyyyyyyyyyyyyyyyyy</p></div>
    <div class="item placeholder"><div class="item-head"><span>XXXXXXXX</span><span class="price">zzzz</span></div><p>Yyyyyyyyyyyyyyyyyyyyyyyyyyyyyyyyyyyyyyyyyyyyyyyyyyyyyyyyyyyyyyyyyyy</p></div>
  </section>

  <div class="band" style="left:25px;top:640px;width:416px"><span class="band-fill" role="img" aria-label="Mint geometric pattern band"></span><h2>MUSHU &amp; RICE</h2></div>

  <section class="section col-left" style="top:682px;width:403px">
    <div class="item"><div class="item-head"><span>Crab And Asparagus Fried Rice</span><span class="price">13.95</span></div><p>White fried rice with dungeness crab, asparagus, and egg white topped with fried onions. No soy sauce.</p></div>
    <div class="item"><div class="item-head"><span>Yang Chow Rice</span><span class="price">9.25</span></div><p>White fried rice with shrimp, barbeque pork, peas, carrots, and eggs. No soy sauce.</p></div>
    <div class="item"><div class="item-head"><span>Mushu</span><span class="price">7.95</span></div><p>Chicken, pork, or vegetable mushu with sautéed vegetables, mushrooms, and eggs. Wrapped in two thin pancakes.<br>For shrimp,add $1.00.</p></div>
    <div class="item"><div class="item-head"><span>Fried Rice</span><span class="price">7.95</span></div><p>Chicken, pork, or vegetable with eggs, scallions, and fried rice sauce. For beef or shrimp, add $1.00. For soft tofu, add $1.00. For deep-Fried tofu, add $1.50.</p></div>
    <div class="item"><div class="item-head"><span>Steamed Rice</span><span class="size-grid"><span>SM.</span><span>LG.</span></span></div><div class="sizes"><p>Choice of White or Brown.</p><span class="size-grid"><span>1.25</span><span>1.75</span></span></div></div>
  </section>

  <div class="band" style="left:462px;top:21px;width:415px"><span class="band-fill" role="img" aria-label="Mint geometric pattern band"></span><h2>BEVERAGES</h2></div>

  <section class="section col-right" style="top:64px;width:401px">
    <div class="item" style="margin-bottom:34px"><div class="item-head"><span>Fjordline (Sparkling or Still)</span></div>
      <div class="sizes"><span>Small (375ml</span><span>4.00</span></div>
      <div class="sizes"><span>Large (800ml)</span><span>6.50</span></div></div>
    <div class="item" style="margin-bottom:16px"><div class="item-head"><span>Cola</span><span class="price">2.75</span></div><p>Cola, Diet Cola, Lemon-Lime Soda, Cherry Cola, Orange Soda</p></div>
    <div class="item" style="margin-bottom:16px"><div class="item-head"><span>Lemonade</span><span class="price">3.50</span></div><div class="item-head"><span>Orange &amp; Cranberry Juice</span><span class="price">3.50</span></div></div>
    <div class="item" style="margin-bottom:16px"><div class="item-head"><span>Ironwood French Press Coffee</span><span class="price">3.95</span></div><p>Caffeinated or Decaffeinated</p></div>
    <div class="item"><div class="item-head"><span>Iced Teas</span><span class="price">2.75</span></div><p>Traditional, Mango, Blackberry Jasmine Green.</p></div>
  </section>

  <div class="band" style="left:462px;top:342px;width:415px"><span class="band-fill" role="img" aria-label="Mint geometric pattern band"></span><h2>LEAF &amp; KETTLE BY THE POT</h2></div>

  <section class="section col-right teas" style="top:382px">
    <div class="item"><div class="item-head"><span>Green Kukicha Tea</span><span class="price">3.75</span></div><p>Often enjoyed for its health benefits, this tea has a fresh green, grassy taste with a crisp finish.</p></div>
    <div class="item"><div class="item-head"><span>Ginger Ginseng Tea</span><span class="price">3.75</span></div><p>This unique chamomile blend is velvety, yet mellow with a complex finish of cinnamon, apple, and lime. Caffeine-Free.</p></div>
    <div class="item"><div class="item-head"><span>White Coconut Crème</span><span class="price">3.75</span></div><p>Tender white peony leaves blended with cornflower, safflower, and sweet creamy coconut.</p></div>
    <div class="item"><div class="item-head"><span>Wuyi Oolong Tea</span><span class="price">3.75</span></div><p>Long beautiful leaves unwind and unfurl when steeped to release a smooth, rice flavor with crisp and earthy tones.</p></div>
    <div class="item"><div class="item-head"><span>Premium Halo Tea</span><span class="price">4.25</span></div><p>Hand-Tied white tea blossoms into a rainbow of jasmine and amaranth flowers with fresh fruit notes.</p></div>
    <div class="item"><div class="item-head"><span>Fjordline Water</span><span class="price">0.00</span></div><p>Sparkling or flat. Small 375 ml $4.00.Large 800 ml $6.00.</p></div>
    <div class="item"><div class="item-head"><span>Jasmine Reserve Tea</span><span class="price">3.75</span></div><p>Organic fair trade green tea repeatedly baked and scented with fresh and fragrant jasmine blossoms.</p></div>
    <div class="item"><div class="item-head"><span>English Breakfast Tea</span><span class="price">3.75</span></div><p>A smooth malty brew with a clean finish, this is Leaf &amp; Kettle's traditional blend of organic black tea.</p></div>
    <div class="item"><div class="item-head"><span>Chamomile Clementine Tea</span><span class="price">3.75</span></div><p>This unique chamomile blend is velvety, yet mellow with a complex finish of cinnamon, apple, and lime. Caffeine-Free.</p></div>
  </section>

  <footer>
    <div class="footer-left"></div>
    <div class="footer-right"></div>
    <div class="brand">Bao<br>Lotus</div>
  </footer>
</main>
</body>
</html>
```